Trucking company specializing in intermodal containers

We need a logo design for our trucking company based in Kent, Washington. Our companies name is Marrow Haulworks LLC, we specialize in intermodal containers, and work off of the Crestline Bay railroads and the ports. We provide service by transporting freight with our fleet of trucks. We operate within Washington, Oregon, and Idaho. Our fleet consists of an east division and a local division. Our team motto currently is globally connected, locally invested.

Target Market(s)

brokers, intermodal management companies, customers

Industry/Entity Type

Trucking Company

Contact Information for Business Card

physical address 4619 N. 312th Pl Kent, WA 98417
office number is 253-518-4096

Font styles to use
Sans Serif

Colors

Designer to choose colors to be used in the design.

Requirements
Must have
• We need to update our current logo. Something like an emblem; that makes a statement that this logo/ sign represents Marrow Haulworks. Something like a royal stamp but in this case a royal shield.
Nice to have
• simple, yet bold. something someone does not currently have. We need something fresh and exciting. Something that will also make a statement because currently our reputation is great within the industry and our community. But we need to reflect that we are professional and willing to provide the best service. We are open to new statement lines.
Should not have
• Should not have something thats been used before. We are open to suggestions that you have and a design that is completely unique and you make originally without what we want but what you like as well. Ofcourse it should still represent the industry we are in.

```html
<!DOCTYPE html>
<html lang="en">
<head>
<meta charset="utf-8">
<title>Marrow Haulworks LLC – Business Cards</title>
<link rel="stylesheet" href="https://fonts.googleapis.com/css2?family=Source+Sans+3:wght@400;700&display=swap">
<style>
  :root {
    --stage-light: #dcdcdc;
    --stage-dark: #ababab;
    --card-white: #ffffff;
    --ink: #111111;
    --brand-red: #d40000;
    --card-black: #000000;
    --edge-red: #7a1010;
  }
  * { margin: 0; padding: 0; box-sizing: border-box; }
  html, body { width: 1200px; height: 1200px; overflow: hidden; }
  body {
    position: relative;
    font-family: "Source Sans 3", sans-serif;
    background: radial-gradient(circle at 50% 50%, var(--stage-light) 0%, var(--stage-dark) 75%);
    color: var(--ink);
  }
  .card {
    position: absolute;
    left: 216px;
    width: 796px;
    height: 453px;
    overflow: hidden;
  }
  .card--front { top: 135px; background: var(--card-white); }
  .card--back {
    top: 614px;
    background: var(--card-black);
    border: 1px solid var(--edge-red);
  }
  .brand-name {
    position: absolute;
    font-weight: 700;
    text-transform: uppercase;
    line-height: 1.05;
    letter-spacing: 0.02em;
  }
  .card--front .brand-name {
    left: 65px; top: 150px;
    font-size: 38px;
    color: var(--ink);
  }
  .card--back .brand-name {
    left: 0; right: 0; top: 115px;
    text-align: center;
    font-size: 60px;
    color: var(--card-white);
  }
  .contact {
    position: absolute;
    left: 414px; top: 40px;
    font-size: 22px;
    line-height: 30px;
  }
  .contact__name { font-size: 33px; font-weight: 700; line-height: 38px; }
  .contact__title { margin-left: 3px; margin-bottom: 24px; }
  .contact__row { display: flex; margin-left: 3px; }
  .contact__label { width: 38px; }
  .contact__row--address { margin-top: 16px; }
  .contact__row--web { margin-top: 20px; }
  .band-red {
    position: absolute; left: 0; right: 0; top: 381px; height: 12px;
    background: var(--brand-red);
  }
  .band-black {
    position: absolute; left: 0; right: 0; top: 401px; bottom: 0;
    background: var(--card-black);
  }
  .web-address {
    position: absolute; left: 0; right: 0; top: 386px;
    text-align: center;
    color: var(--card-white);
    font-size: 25px;
    letter-spacing: 0.3em;
  }
</style>
</head>
<body>
  <section class="card card--front" aria-label="Business card front">
    <div class="brand-name">Marrow<br>Haulworks LLC</div>
    <div class="contact">
      <div class="contact__name">Your Full Name</div>
      <div class="contact__title">Your Title</div>
      <div class="contact__row"><span class="contact__label">P</span><span>: 253-518-4096</span></div>
      <div class="contact__row"><span class="contact__label">M</span><span>: 012-345-6789</span></div>
      <div class="contact__row"><span class="contact__label">E</span><span>: your email address</span></div>
      <div class="contact__row contact__row--address"><span class="contact__label">A</span><span>: 4619 N. 312th Pl Kent,<br>&nbsp;&nbsp;WA 98417</span></div>
      <div class="contact__row contact__row--web"><span>W : www.marrowhaulworks.com</span></div>
    </div>
    <div class="band-red"></div>
    <div class="band-black"></div>
  </section>

  <section class="card card--back" aria-label="Business card back">
    <div class="brand-name">Marrow<br>Haulworks LLC</div>
    <div class="web-address">www.marrowhaulworks.com</div>
  </section>
</body>
</html>
```